Town Planning Consultants require lstationary design

Require a design to be used for our letterhead and report cover page. We have an approved logo.
we have attached our logo, and our temporary letterhead/cover page (SEE Cover) which we currently adapt for both purposes in the interim pending a permanent design. I have also attached an example (example report cover) of a report cover page that I like. perhaps similar with our colour scheme

Target Market(s)

?

Industry/Entity Type

Town

Colors
249fd4
3176b5

Requirements
Must have
• colours to match logo
• the text content in existing letterhead

```html
<!DOCTYPE html>
<html lang="en">
<head>
<meta charset="utf-8">
<title>Corella Planning – Stationery Set</title>
<link href="https://fonts.googleapis.com/css2?family=Arimo:wght@400;700&family=Oswald:wght@600&display=swap" rel="stylesheet">
<style>
  :root{
    --bg:#3b3b3d;
    --paper:#ffffff;
    --brand:#3f8fd2;
    --brand-deep:#3176b5;
    --panel:#5b9bd5;
    --panel-dark:#4a78bd;
    --ink:#2b2b2b;
    --muted:#555;
    --rule:#9ec4e6;
    --date:#7fb3e3;
  }
  *{margin:0;padding:0;box-sizing:border-box}
  html,body{width:1200px;height:1200px;overflow:hidden;background:var(--bg)}
  body{position:relative;font-family:'Arimo',Arial,sans-serif;color:var(--ink)}
  .sheet{position:absolute;background:var(--paper);box-shadow:0 2px 6px rgba(0,0,0,.35)}
  .brand-name{font-family:'Arimo',Arial,sans-serif;font-weight:400;color:var(--brand);white-space:nowrap;line-height:1}
  .contact{position:absolute;list-style:none;color:var(--ink);line-height:1.3}
  .contact li{display:flex;align-items:flex-start;gap:4px}
  .contact svg{flex:none;margin-top:1px}
  .contact.divided{border-left:1px dashed var(--brand);padding-left:7px}

  /* business card front */
  .card-front{left:131px;top:115px;width:268px;height:147px;border-bottom:5px solid var(--panel)}
  .card-front .brand-name{position:absolute;left:17px;top:26px;font-size:17px}
  .card-front .holder{position:absolute;left:17px;top:88px;font-size:12.5px;color:var(--brand)}
  .card-front .role{position:absolute;left:17px;top:103px;font-size:9px;color:var(--muted)}
  .card-front .contact{left:150px;top:79px;font-size:6.4px}

  /* business card back */
  .card-back{left:131px;top:282px;width:270px;height:149px;background:var(--panel);display:flex;align-items:center;justify-content:center}
  .card-back .brand-name{color:#fff;font-size:27px}

  /* envelope */
  .envelope{left:627px;top:139px;width:496px;height:250px}
  .envelope .brand-name{position:absolute;left:30px;top:52px;font-size:25px}
  .envelope .contact{left:38px;top:168px;font-size:8.6px}

  /* letterhead */
  .letterhead{left:139px;top:460px;width:434px;height:614px}
  .letterhead .brand-name{position:absolute;left:54px;top:60px;font-size:22px}
  .letterhead .contact{left:278px;top:40px;font-size:6.6px}
  .letter-body{position:absolute;left:54px;top:170px;width:325px;font-size:6.6px;line-height:10.2px;color:var(--muted)}
  .letter-body .date{font-weight:700;font-size:8.6px;color:var(--ink);margin-bottom:8px}
  .letter-body p{margin-bottom:9px}
  .letter-body .signoff{margin-top:18px}
  .signature{display:block;width:62px;height:30px;margin:8px 0 10px;background:#eef1f5}
  .signer{font-weight:700;color:var(--ink)}

  /* report cover */
  .cover{left:636px;top:460px;width:434px;height:614px;overflow:hidden}
  .cover-shapes{position:absolute;inset:0;width:100%;height:100%}
  .cover .brand-name{position:absolute;left:0;right:0;top:88px;text-align:center;font-size:32px}
  .cover-text{position:absolute;left:47px;top:268px;width:340px;color:#fff}
  .cover-text .kicker{font-size:7.4px;font-weight:700;letter-spacing:.2px;color:#1f2c3d}
  .cover-text h1{font-family:'Oswald',Impact,sans-serif;font-weight:600;font-size:21px;line-height:25px;margin-top:7px;letter-spacing:-.3px;text-transform:uppercase}
  .cover-text .subject{font-size:15.5px;color:#1f2c3d;margin-top:40px}
  .cover-text .divider{height:1px;background:#d8e8f6;margin-top:14px}
  .cover-text .site{font-size:7.8px;font-weight:700;color:#1f2c3d;margin-top:11px}
  .cover .issue-date{position:absolute;right:32px;bottom:30px;font-size:8.6px;color:var(--date)}
</style>
</head>
<body>

<svg width="0" height="0" style="position:absolute" aria-hidden="true">
  <defs>
    <symbol id="i-pin" viewBox="0 0 10 10"><path d="M5 .5a3.3 3.3 0 0 0-3.3 3.3C1.7 6.3 5 9.5 5 9.5s3.3-3.2 3.3-5.7A3.3 3.3 0 0 0 5 .5zm0 4.6a1.3 1.3 0 1 1 0-2.6 1.3 1.3 0 0 1 0 2.6z" fill="#3f8fd2"/></symbol>
    <symbol id="i-phone" viewBox="0 0 10 10"><path d="M2.2.8l1.6 1.9-.8 1.2c.6 1.2 1.6 2.2 2.9 2.9l1.2-.8 1.9 1.6-.9 1.5C4.6 9.1.9 5.4.7 1.7z" fill="#3f8fd2"/></symbol>
    <symbol id="i-mobile" viewBox="0 0 10 10"><rect x="2.7" y=".6" width="4.6" height="8.8" rx=".8" fill="none" stroke="#3f8fd2" stroke-width="1"/></symbol>
    <symbol id="i-mail" viewBox="0 0 10 10"><rect x=".8" y="2.3" width="8.4" height="5.6" fill="#3f8fd2"/><path d="M.8 2.5 5 5.6l4.2-3.1" fill="none" stroke="#fff" stroke-width=".8"/></symbol>
  </defs>
</svg>

<section class="sheet card-front">
  <div class="brand-name">Corella Planning</div>
  <div class="holder">M.Harlow</div>
  <div class="role">Owner</div>
  <ul class="contact divided">
    <li><svg width="6" height="6"><use href="#i-pin"/></svg><span>12 Harbour Ridge Road,<br>COOMBAH&nbsp; NSW 2499</span></li>
    <li><svg width="6" height="6"><use href="#i-phone"/></svg><span>+61 (2) 5550 1234</span></li>
    <li><svg width="6" height="6"><use href="#i-mobile"/></svg><span>+61 (0)400 555 018</span></li>
    <li><svg width="6" height="6"><use href="#i-mail"/></svg><span>info@corellaplanning.com.au</span></li>
  </ul>
</section>

<section class="sheet card-back">
  <div class="brand-name">Corella Planning</div>
</section>

<section class="sheet envelope">
  <div class="brand-name">Corella Planning</div>
  <ul class="contact">
    <li><svg width="8" height="8"><use href="#i-pin"/></svg><span>12 Harbour Ridge Road,<br>COOMBAH&nbsp; NSW 2499</span></li>
    <li><svg width="8" height="8"><use href="#i-phone"/></svg><span>+61 (2) 5550 1234</span></li>
    <li><svg width="8" height="8"><use href="#i-mobile"/></svg><span>+61 (0)400 555 018</span></li>
    <li><svg width="8" height="8"><use href="#i-mail"/></svg><span>info@corellaplanning.com.au</span></li>
  </ul>
</section>

<section class="sheet letterhead">
  <div class="brand-name">Corella Planning</div>
  <ul class="contact divided">
    <li><svg width="6" height="6"><use href="#i-pin"/></svg><span>12 Harbour Ridge Road,<br>COOMBAH&nbsp; NSW 2499</span></li>
    <li><svg width="6" height="6"><use href="#i-phone"/></svg><span>+61 (2) 5550 1234</span></li>
    <li><svg width="6" height="6"><use href="#i-mobile"/></svg><span>+61 (0)400 555 018</span></li>
    <li><svg width="6" height="6"><use href="#i-mail"/></svg><span>info@corellaplanning.com.au</span></li>
  </ul>
  <div class="letter-body">
    <div class="date">Aug 16, 2016</div>
    <p>Lorem ipsum. Proin gravida nibh vel velit auctor aliquet. Aenean sollicitudin, lorem quis bibendum auctor, nisi elit consequat ipsum, nec sagittis sem nibh id elit. Duis sed odio sit amet nibh vulputate cursus a sit amet mauris. Morbi accumsan ipsum velit. Nam nec tellus a odio tincidunt auctor a ornare odio. Sed non mauris vitae erat consequat auctor eu in elit. Class aptent taciti sociosqu ad litora torquent per conubia nostra, per inceptos himenaeos. Mauris in erat justo. Nullam ac urna eu felis dapibus condimentum sit amet a augue. Sed non neque elit. Sed ut imperdiet nisi. Proin condimentum fermentum nunc. Etiam pharetra, erat sed fermentum feugiat, velit mauris egestas quam, ut aliquam massa nisl quis neque. Suspendisse in orci enim.</p>
    <p>Lorem ipsum. Proin gravida nibh vel velit auctor aliquet. Aenean sollicitudin, lorem quis bibendum auctor, nisi elit consequat ipsum, nec sagittis sem nibh id elit. Duis sed odio sit amet nibh vulputate cursus a sit amet mauris. Morbi accumsan ipsum velit. Nam nec tellus a odio tincidunt auctor a ornare odio. Sed non mauris vitae erat consequat auctor eu in elit. Class aptent taciti sociosqu ad litora torquent per conubia nostra, per inceptos himenaeos. Mauris in erat justo. Nullam ac urna eu felis dapibus condimentum sit amet a augue. Sed non neque elit. Sed ut imperdiet nisi. Proin condimentum fermentum nunc. Etiam pharetra, erat sed fermentum feugiat, velit mauris egestas quam, ut aliquam massa nisl quis neque. Suspendisse in orci enim.</p>
    <div class="signoff">Kind Regards,</div>
    <span class="signature" role="img" aria-label="Handwritten signature"></span>
    <div class="signer">M.Harlow</div>
    <div>Owner and Principal</div>
  </div>
</section>

<section class="sheet cover">
  <svg class="cover-shapes" viewBox="0 0 543 767" preserveAspectRatio="none" aria-hidden="true">
    <polygon points="0,253 543,323 543,643 0,760" fill="var(--panel)"/>
    <polygon points="170,275 543,214 543,323" fill="var(--panel-dark)"/>
  </svg>
  <div class="brand-name">Corella Planning</div>
  <div class="cover-text">
    <div class="kicker">DEVELOPMENT APPLICATION</div>
    <h1>Statement of<br>Environmental Effects</h1>
    <div class="subject">Proposed Additions to Existing Dwelling</div>
    <div class="divider"></div>
    <div class="site">14 Linden Street, NORTHBRIDGE</div>
  </div>
  <div class="issue-date">JUNE, 2016</div>
</section>

</body>
</html>
```